VOLTIQ4 Website design (Need help to re-design our website)

We need someone to help us re-design our website and launch it. All contents for the website are ready. (Website: https://www.voltiq4.com.au/)

-Rearrange categories:
1. Heat Pumps (Link to KALVO site: https://kalvo.com.au/)
2. Solar (Under the Solar category; remove solar panels, solar inverters, and solar batteries)
3. LED
4. Capability Statement
5. Service and Support
6. Contact us

Home page - redesign but the free quote will stay.

NOTE:
-Try using professional fonts (Example: Helvetica, etc.)
-Try to play with colours related to sustainability, eco-friendliness, solar, energy, and energy efficiency.
-The website's Footer should be readable and use light colour.

Target Market(s)

Residentials & commercial buildings

Industry/Entity Type

SOLAR ENERGY PROVIDER

Coding

Coded - Design and coding required

Colors

Designer to choose colors to be used in the design.

Requirements
Nice to have
• Effects/transition on the words/copy/images.

```html
<!DOCTYPE html>
<html lang="en">
<head>
<meta charset="utf-8">
<title>VOLTIQ4 – Next Generation Energy Saving Products</title>
<link href="https://fonts.googleapis.com/css2?family=Archivo:wght@400;500;600;700;800&family=Montserrat:wght@500;600;700&display=swap" rel="stylesheet">
<style>
:root{
  --blue:#1565c0;--blue-dark:#0d3c8c;--navy:#0b1f4f;--sky:#0e9be0;
  --green:#6cb33f;--green-dark:#2e8b3a;--grey:#efefef;--grey-2:#e6e6e6;
  --ink:#222;--text:#555;--white:#fff;
}
*{box-sizing:border-box;margin:0;padding:0}
html,body{width:1200px;height:4342px;overflow:hidden}
body{font-family:"Archivo",Helvetica,Arial,sans-serif;color:var(--ink);background:var(--white);position:relative}
.abs{position:absolute}
.ph{position:absolute;border-radius:8px}
.logo{display:flex;align-items:center;gap:8px}
.logo-mark{width:26px;height:26px;border-radius:50%;background:var(--green)}
.logo-name{font-weight:800;font-size:26px;color:var(--blue);letter-spacing:.5px}
.logo-tag{font-size:7px;color:var(--text);margin-top:-2px}
.site-header{top:0;left:0;width:1200px;height:62px;background:#fff;border-top:3px solid var(--blue)}
.nav{position:absolute;left:398px;top:24px;display:flex;gap:32px;font-size:11px;color:#666;letter-spacing:.3px}
.btn-contact{position:absolute;left:937px;top:18px;width:138px;height:32px;border-radius:16px;background:var(--blue);color:#fff;font-size:11px;font-weight:700;display:flex;align-items:center;padding-left:24px}
.dot{width:24px;height:24px;border-radius:50%;background:var(--green);position:absolute;right:4px;top:4px;display:flex;align-items:center;justify-content:center}
.hero{top:62px;left:0;width:1200px;height:541px;background:linear-gradient(180deg,#6b9fd3 0%,#a9c4de 35%,#4b6b8c 60%,#1d3b5e 100%)}
.hero h1{position:absolute;left:120px;top:86px;font-size:44px;font-weight:800;color:#fff;line-height:1.15}
.hero h1 span{color:var(--green)}
.hero p{position:absolute;left:120px;top:196px;color:#fff;font-size:13px}
.quote{position:absolute;left:793px;top:90px;width:285px;height:302px;background:#fff;padding:12px}
.quote h3{background:var(--green);color:#fff;text-align:center;font-size:17px;font-weight:700;padding:7px 0;margin-bottom:10px}
.field{height:24px;border:1px solid #ccc;font-size:9px;color:#888;padding:6px 12px;margin:0 0 9px;display:flex;justify-content:space-between}
.submit{margin:14px 12px 0;height:34px;background:var(--blue);border-radius:4px;color:#fff;font-weight:700;font-size:11px;display:flex;align-items:center;justify-content:center;position:relative}
.accred{top:603px;left:0;width:1200px;height:172px;background:var(--grey)}
.accred h2{position:absolute;left:120px;top:55px;font-size:20px;font-weight:700;line-height:1.3}
.badge{position:absolute;top:50px;height:55px;border-radius:6px;background:#d8d8d8}
.services{top:775px;left:0;width:1200px;height:460px;background:#fff}
.sec-title{text-align:center;font-size:31px;font-weight:700;color:var(--ink)}
.card{position:absolute;top:110px;width:305px;height:298px;background:var(--grey);border-radius:8px;border-bottom:4px solid var(--green);text-align:center;overflow:hidden;box-shadow:0 2px 6px rgba(0,0,0,.12)}
.card .ph{position:static;height:175px;border-radius:0}
.card h4{font-size:15px;font-weight:600;margin:14px 0 6px}
.card p{font-size:10px;color:var(--text);line-height:1.4;padding:0 30px}
.card a{display:block;margin-top:8px;font-size:11px;font-weight:600;color:var(--blue)}
.solar{top:1235px;left:0;width:1200px;height:1048px;background:var(--grey)}
.feature-img{position:absolute;width:658px;height:265px;border-radius:12px;box-shadow:6px 6px 0 var(--green)}
.feature h3{font-size:21px;font-weight:600;margin-bottom:14px}
.feature p{font-size:10.5px;color:var(--text);line-height:1.45;margin-bottom:12px}
.feature{position:absolute;width:275px}
.read{display:inline-flex;align-items:center;height:30px;padding:0 30px 0 6px;background:var(--blue);color:#fff;font-size:10px;font-weight:700;border-radius:15px 0 0 15px;clip-path:polygon(0 0,85% 0,100% 100%,0 100%);gap:16px}
.read i{width:22px;height:22px;border-radius:50%;background:var(--green)}
.heat{top:2283px;left:0;width:1200px;height:422px;background:linear-gradient(90deg,#f0a24a 0%,#6b6f86 35%,#16265a 65%,#0b1a44 100%)}
.heat h2{position:absolute;left:727px;top:165px;font-size:30px;color:#fff;font-weight:700}
.heat p{position:absolute;left:727px;top:210px;width:355px;color:#fff;font-size:10.5px;line-height:1.45}
.clients{top:2705px;left:0;width:1200px;height:215px;background:linear-gradient(180deg,var(--sky),#0a7fd0)}
.clients h2{text-align:center;color:#fff;font-size:21px;font-weight:600;margin-top:48px}
.client{position:absolute;top:95px;width:140px;height:60px;display:flex;align-items:center;justify-content:center;gap:6px;color:#fff;font-weight:700;font-size:15px}
.client b{width:12px;height:12px;background:#fff;border-radius:50%}
.about{top:2920px;left:0;width:1200px;height:450px;background:#fff}
.about h2{position:absolute;left:195px;top:105px;font-size:31px;font-weight:700}
.about .copy{position:absolute;left:195px;top:150px;width:330px;font-size:10px;color:var(--text);line-height:1.5}
.about .copy p{margin-bottom:14px}
.reviews{top:3370px;left:0;width:1200px;height:472px;background:#ececec}
.reviews h2{position:absolute;left:118px;top:62px;font-size:31px;font-weight:700}
.rating{position:absolute;left:888px;top:52px;display:flex;gap:10px;align-items:center}
.rating .circ{width:38px;height:38px;border-radius:50%;background:#fff;border:4px solid var(--blue)}
.stars{color:#f5b301;font-size:15px;letter-spacing:2px}
.rev{position:absolute;top:125px;width:222px;height:290px;background:#fff;border-radius:8px;box-shadow:0 2px 6px rgba(0,0,0,.12);padding:20px 18px}
.rev p{font-size:10.5px;color:var(--text);line-height:1.6;margin-top:10px}
.rev .who{position:absolute;left:18px;bottom:26px;display:flex;align-items:center;gap:10px;font-family:"Montserrat",sans-serif;font-size:12px;font-weight:600}
.who i{width:34px;height:34px;border-radius:50%;background:#9aa8b8}
.rev .g{position:absolute;right:16px;top:18px;width:16px;height:16px;border-radius:50%;border:3px solid var(--blue)}
.arrow{position:absolute;top:265px;width:22px;height:22px;border-radius:50%;background:var(--blue);color:#fff;font-size:13px;display:flex;align-items:center;justify-content:center}
.signup{top:3842px;left:0;width:1200px;height:253px;background:linear-gradient(90deg,#2e9e45,#1c6f3a)}
.signup h2{position:absolute;width:100%;top:98px;text-align:center;color:#fff;font-size:30px;font-weight:700}
.signup p{position:absolute;width:100%;top:138px;text-align:center;color:#fff;font-size:12px}
.sub-box{position:absolute;left:372px;top:168px;width:456px;height:40px;background:#fff;border-radius:20px;font-size:11px;color:#333;padding:13px 26px}
.sub-btn{position:absolute;right:-8px;top:0;height:40px;width:150px;background:var(--blue);color:#fff;font-weight:700;font-size:10px;display:flex;align-items:center;padding-left:46px;clip-path:polygon(0 0,88% 0,100% 100%,0 100%);border-radius:20px 0 0 20px}
.footer{top:4095px;left:0;width:1200px;height:221px;background:#fff}
.fcol{position:absolute;top:30px}
.fcol h5{font-size:15px;font-weight:700;margin-bottom:12px;color:var(--ink)}
.fcol li{list-style:none;font-size:9px;color:#333;margin-bottom:9px;display:flex;align-items:center;gap:10px}
.ic{width:20px;height:20px;border-radius:50%;background:var(--blue);flex:none;display:flex;align-items:center;justify-content:center}
.vline{position:absolute;top:30px;width:1px;height:170px;background:#c8d4ea}
.bottom-bar{top:4316px;left:0;width:1200px;height:26px;background:var(--blue);color:#fff;font-size:9px;display:flex;align-items:center;justify-content:space-between;padding:0 120px}
</style>
</head>
<body>

<header class="abs site-header">
  <div class="abs logo" style="left:120px;top:12px">
    <div class="logo-mark"></div>
    <div><div class="logo-name">VOLTIQ4</div><div class="logo-tag">Next Generation Energy Products</div></div>
  </div>
  <nav class="nav"><span>HEAT PUMPS</span><span>SOLAR ▾</span><span>LED</span><span>CAPABILITY STATEMENT</span><span>SERVICES &amp; SUPPORT</span></nav>
  <div class="btn-contact">CONTACT US<span class="dot"></span></div>
</header>

<section class="abs hero">
  <div role="img" aria-label="Rows of solar panels in a field under a cloudy sky" style="position:absolute;inset:0"></div>
  <h1>WHY PAY <span>EXCESS</span> FOR<br>YOUR ELECTRICITY?</h1>
  <p>Save on electricity costs by switching to solar!</p>
  <form class="quote">
    <h3>WANT A FREE QUOTE?</h3>
    <div class="field">Name</div><div class="field">Email</div><div class="field">Phone</div><div class="field">Address</div>
    <div class="field"><span>I am Interested in</span><span>⌄</span></div>
    <div class="field"><span>How Did You Find Us</span><span>⌄</span></div>
    <div class="submit">SUBMIT<span class="dot" style="top:5px"></span></div>
  </form>
  <svg class="abs" style="left:0;bottom:0" width="1200" height="90" viewBox="0 0 1200 90">
    <polygon points="0,40 600,85 1200,20 1200,90 0,90" fill="#efefef"/>
    <polyline points="0,30 600,82 1200,10" fill="none" stroke="#6cb33f" stroke-width="10"/>
  </svg>
</section>

<section class="abs accred">
  <h2>ACCREDITATIONS<br>&amp; PARTNERS</h2>
  <div class="badge" style="left:348px;width:40px"></div>
  <div class="badge" style="left:448px;width:95px;height:45px;top:55px"></div>
  <div class="badge" style="left:602px;width:46px;border-radius:50%"></div>
  <div class="badge" style="left:692px;width:105px;border-radius:28px"></div>
  <div class="badge" style="left:858px;width:44px;border-radius:50%"></div>
  <div class="badge" style="left:938px;width:140px;height:30px;top:62px;border-radius:15px"></div>
</section>

<section class="abs services">
  <h2 class="sec-title" style="margin-top:50px">OUR SERVICES &amp; SUPPORT</h2>
  <div class="card" style="left:120px"><div class="ph" role="img" aria-label="Technician cleaning a solar panel" style="background:linear-gradient(135deg,#8fb3d9,#2d4f7e)"></div><h4>Solar Panel Cleaning</h4><p>Solar panels are great, but panels become dirty, then their power output and efficiency is reduced, sometimes up to 15%-25%.</p><a>Read More ⟶</a></div>
  <div class="card" style="left:446px"><div class="ph" role="img" aria-label="Hands repairing an inverter circuit board" style="background:linear-gradient(135deg,#4aa59a,#1f3f4a)"></div><h4>Inverter Repairs &amp; Warranty</h4><p>Fixing up an inverter may simply take a read through your inverter's manual or filling up a Repair Request from your warranty provider.</p><a>Read More ⟶</a></div>
  <div class="card" style="left:772px"><div class="ph" role="img" aria-label="Solar panels with battery and inverter package" style="background:linear-gradient(135deg,#d9d9d9,#555)"></div><h4>Solar Package Repair</h4><p>While most solar system installations have been designed to be as durable and long-lasting as possible, there is sometimes maintenance.</p><a>Read More ⟶</a></div>
</section>

<section class="abs solar">
  <h2 class="sec-title" style="margin-top:50px">SOLAR</h2>
  <div class="feature-img" role="img" aria-label="Close-up of blue solar panels against the sky" style="left:120px;top:122px;background:linear-gradient(135deg,#4c8fd6,#0c2f6b)"></div>
  <div class="feature" style="left:802px;top:178px"><h3>Remove solar Panels</h3><p>Solar panels are great, but panels become dirty, then their power output and efficiency is reduced, sometimes up to 15%-25%. Dust on solar panels does a lot more than make them look old, 4 grams of dust per square meter can decrease solar power connection by up to 30%.</p><span class="read"><i></i>READ MORE</span></div>
  <div class="feature-img" role="img" aria-label="Row of solar inverters installed outdoors" style="left:420px;top:440px;background:linear-gradient(135deg,#6d8fb8,#39404a)"></div>
  <div class="feature" style="left:120px;top:510px;width:245px"><h3>Solar inverters</h3><p>Inverters play a pivotal job in any solar powered energy system and is responsible for inverting DC output of a solar panel into an AC current.</p><span class="read"><i></i>READ MORE</span></div>
  <div class="feature-img" role="img" aria-label="Solar panel on a grassy field with battery units" style="left:120px;top:758px;background:linear-gradient(180deg,#6e86d8,#b9c8ee 45%,#5f9a4a)"></div>
  <div class="feature" style="left:822px;top:800px"><h3>Solar Batteries</h3><p>A simple grid connected solar system does not need batteries to function. But your solar system might be generating more energy than required.</p><p>A solar battery is be a good option for those who want to use their own electricity production during off peak hours or on cloudy days.</p><span class="read"><i></i>READ MORE</span></div>
</section>

<section class="abs heat">
  <div role="img" aria-label="Heat pump water heaters in front of solar panels at sunset" style="position:absolute;left:0;top:0;width:640px;height:422px"></div>
  <svg class="abs" style="left:0;top:0" width="1200" height="80" viewBox="0 0 1200 80">
    <polygon points="0,0 1200,0 1200,6 600,70 0,20" fill="#efefef"/>
    <polyline points="0,16 600,66 1200,2" fill="none" stroke="#1565c0" stroke-width="10"/>
  </svg>
  <h2>HEAT PUMP</h2>
  <p>Heat pump water heaters use electricity to take out the surrounding air and flow it through the pump, causing the temperature to increase, and is then circulated into the water tank ready to be used for hot water heating.<br><br>In essence, a heat pump water heater works just like an air conditioner, but in reverse. Instead of pulling the hot air from the inside and dumping it outside, a heat pump water heater draws in ambient air from the outside and warms it up inside.</p>
</section>

<section class="abs clients">
  <h2>OUR CLIENTS</h2>
  <div class="client" style="left:120px"><b></b>Hillcrest Fencing</div>
  <div class="client" style="left:302px"><b></b>Tessaline Labs</div>
  <div class="client" style="left:465px"><b></b>Parcelway</div>
  <div class="client" style="left:620px"><b></b>Courtside Club</div>
  <div class="client" style="left:790px"><b></b>Ironbark Steel</div>
  <div class="client" style="left:950px"><b></b>Safeguard Co</div>
</section>

<section class="abs about">
  <h2>ABOUT VOLTIQ4</h2>
  <div class="copy">
    <p>At VOLTIQ4, we trust in our products, our team and our knowledge to ensure the best possible experience when you switch to solar.</p>
    <p>Power bills have risen dramatically in Australia over the past decade and energy bills are now among the highest home expenses and business operating expenses for most government, civil and commercial organisations.</p>
    <p>Whether you own or run a business and want to reduce your electricity bills, or just cut energy consumption in the home, we would be delighted to help give you an VOLTIQ4 experience.</p>
    <span class="read" style="margin-top:6px"><i></i>READ MORE</span>
  </div>
  <div class="feature-img" role="img" aria-label="Wind turbine above solar panels under blue sky" style="left:620px;top:90px;width:458px;height:300px;background:linear-gradient(160deg,#5aa8ea,#0b3a7a)"></div>
</section>

<section class="abs reviews">
  <h2>HEAR WHAT OUR CLIENTS SAY</h2>
  <div class="rating"><div class="circ"></div><div><div><span class="stars">★★★★★</span> <b style="font-size:13px">4.9 / 5.0</b></div><div style="font-size:10px;color:#555">Based on verified reviews</div></div></div>
  <div class="arrow" style="left:86px">‹</div><div class="arrow" style="left:1088px">›</div>
  <div class="rev" style="left:122px"><span class="stars">★★★★★</span><span class="g"></span><p>Happy with everything. I got a very good product with a very reasonable price. Also, they help me a lot through all the process, especially on the rebate application process. Very professional and knowledgeable.</p><div class="who"><i></i>Priya Kamal</div></div>
  <div class="rev" style="left:366px"><span class="stars">★★★★★</span><span class="g"></span><p>I am very happy with VOLTIQ4 solar install in my place in Brisbane. Their rates were the most competitive when I shopped around. Their before install and post install process was very smooth. I would recommend going with them.</p><div class="who" style="bottom:62px"><i></i>Rohan Mehra</div></div>
  <div class="rev" style="left:610px"><span class="stars">★★★★★</span><span class="g"></span><p>I have been dealing with this company for the past 2 years and have found they are very prompt, engaging with customers and contractors, very transparent and competitive within the market. Would highly recommend their services to anyone.</p><div class="who" style="bottom:44px"><i></i>Daniel</div></div>
  <div class="rev" style="left:853px"><span class="stars">★★★★★</span><span class="g"></span><p>Very happy with the service. VOLTIQ4 delivered what they promised, no hidden cost and very professional. Always replyand answer any questions. Thank you for the great service, I totally recommend to use VOLTIQ4 for your solar.</p><div class="who" style="bottom:72px"><i></i>Lena Tran</div></div>
</section>

<section class="abs signup">
  <svg class="abs" style="left:0;top:0" width="1200" height="80" viewBox="0 0 1200 80">
    <polygon points="0,0 1200,0 1200,60 600,0 0,60" fill="#ececec"/>
    <polyline points="0,62 600,4 1200,62" fill="none" stroke="#1565c0" stroke-width="10"/>
  </svg>
  <h2>SIGN UP FOR THE LATEST OFFERS</h2>
  <p>Get all the latest information on Special Discounts, Products and Offers.</p>
  <div class="sub-box">Enter Your Email Address<span class="sub-btn"><span class="dot" style="left:8px;right:auto;top:8px"></span>SUBSCRIBE</span></div>
</section>

<footer class="abs footer">
  <div class="abs logo" style="left:120px;top:30px"><div class="logo-mark"></div><div><div class="logo-name">VOLTIQ4</div><div class="logo-tag">Next Generation Energy Products</div></div></div>
  <div class="ph" role="img" aria-label="Promotional banner showing an energy product brochure" style="left:122px;top:110px;width:168px;height:82px;border-radius:2px;background:linear-gradient(135deg,#3f7fd0,#dfe8f5)"></div>
  <div class="fcol" style="left:348px"><h5>QUICK LINKS</h5><ul><li>Home</li><li>Heat pumps</li><li>solar</li><li>led</li><li>capability statement</li><li>services &amp; supports</li><li>Contact Us</li></ul></div>
  <div class="vline" style="left:485px"></div>
  <div class="fcol" style="left:510px"><h5>CONTACT US</h5><ul><li><span class="ic"></span>1300 555 014</li><li><span class="ic"></span>Business hours: 9AM - 5PM</li><li><span class="ic"></span>enquiries@voltiq4.com.au</li></ul></div>
  <div class="vline" style="left:685px"></div>
  <div class="fcol" style="left:706px"><h5>CONTACT US</h5><ul><li><span class="ic"></span>24 Wattle Street Ashfield VIC 3030</li><li><span class="ic"></span>5/12 Harbour Road Coomera QLD 4209</li><li><span class="ic"></span>9 Depot Lane Mildura VIC 3500</li><li><span class="ic"></span>110/48 King St, Perth WA 6000</li><li><span class="ic"></span>4/62 Elizabeth Street Hobart TAS 7000</li></ul></div>
  <div class="vline" style="left:950px"></div>
  <div class="fcol" style="left:975px"><h5>FOLLOW US</h5><ul><li><span class="ic"></span>Facepage</li><li><span class="ic"></span>WorkLink</li><li><span class="ic"></span>VidTube</li></ul></div>
</footer>
<div class="abs bottom-bar"><span>© Copyright 2024 VOLTIQ4 All Rights Reserved</span><span>Privacy policy &nbsp;|&nbsp; Terms Of Use &nbsp;|&nbsp; Legal</span></div>

</body>
</html>
```